Skill Up Salary Up

Full Page
7.5 w x 10 h / 8 w x 10.75 h + .25" bleed
Full-Page Career Course Ad
Project Overview
• Goal: Create a visually attractive, modern, and uncluttered full-page magazine advertisement to list available career courses.
• Tone: Creative, professional, and attention-grabbing to prevent the reader from turning the page. The final design must prioritize readability.

Content Requirements
1. Header/Headline: Must be the primary focus. And grab peoples attention
2. Course Listing: A clear, well-organized list of the career courses.
________________________________________
Design & Aesthetic Directives
1. Layout & Readability (Crucial)
• The final ad must not look crowded or busy.
• Prioritize white space to make the text "breathe" and ensure the course list is easy to scan and read.
• Use a modern, clean, and professional typeface (font choice is critical for the aesthetic).
2. Visual Style
• Aim for a creative, modern, and fresh look. Avoid outdated or generic stock imagery/layouts.
3. Imagery/Graphic Element (Artist's Choice)
You have creative freedom regarding the main graphic element.
• Option A (Photography): Use a photo of a white male American with a collared shirt. The imagery should convey success, focus, or professional development.
• Option B (Vector/Illustration): Use a modern vector graphic, illustration, or abstract design. This could be used to symbolize growth, connection, or a career path.
The choice of graphic element is yours, but it must support the overall modern and uncrowded aesthetic.

Requirements
Must have
• Partial listing .. is part of the Vocational Horizon Course

```html
<!DOCTYPE html>
<html lang="en">
<head>
<meta charset="utf-8">
<title>Skill Up Salary Up – Upcoming Summit Courses</title>
<link href="https://fonts.googleapis.com/css2?family=Allura&family=Poppins:wght@400;500;600;700;800&display=swap" rel="stylesheet">
<style>
:root{
  --purple-deep:#3d0656;
  --purple:#4b0a6e;
  --purple-bright:#6a0ea8;
  --yellow:#fdc000;
  --orange:#ff9a00;
  --ink:#3a0654;
  --white:#ffffff;
}
*{margin:0;padding:0;box-sizing:border-box}
html,body{width:972px;height:1200px;overflow:hidden;background:var(--white)}
body{font-family:"Poppins",sans-serif;position:relative}
.ad{position:absolute;inset:0;background:var(--white)}
.band-top{position:absolute;left:0;top:0;width:972px;height:369px;background:radial-gradient(circle at 95% 75%,var(--purple-bright),var(--purple) 45%,var(--purple-deep))}
.band-yellow{position:absolute;left:0;top:369px;width:972px;height:254px;background:var(--yellow)}
.band-lower{position:absolute;left:0;top:623px;width:972px;height:445px;background:radial-gradient(circle at 90% 10%,var(--purple-bright),var(--purple) 40%,var(--purple-deep))}
.abs{position:absolute}
.photo{left:560px;top:62px;width:380px;height:561px;border-radius:190px 190px 0 0;background:linear-gradient(180deg,rgba(255,255,255,.18),rgba(255,255,255,.55) 40%,#f4f1f6)}
.script{left:58px;top:58px;font-family:"Allura",cursive;font-size:92px;color:var(--white);line-height:1;white-space:nowrap}
.headline{left:56px;font-weight:800;line-height:1;letter-spacing:-1px;white-space:nowrap}
.headline.upcoming{top:120px;font-size:96px;background:linear-gradient(180deg,var(--yellow),var(--orange));-webkit-background-clip:text;background-clip:text;color:transparent}
.headline.courses{top:200px;font-size:78px;color:var(--white)}
.perk{top:290px;display:flex;gap:6px;color:var(--white);font-weight:700;font-size:17px;line-height:1.1;text-transform:uppercase}
.perk svg{flex:none;margin-top:2px}
.pill{display:flex;align-items:center;justify-content:center;border-radius:14px;font-weight:700;font-size:23px;white-space:nowrap}
.pill.dark{background:var(--purple);color:var(--white);border:2px solid var(--white)}
.pill.warm{background:linear-gradient(90deg,var(--orange),var(--yellow) 55%,var(--orange));color:var(--ink);box-shadow:0 2px 0 rgba(0,0,0,.15)}
.subhead{font-weight:700;font-size:19px;line-height:1.05;color:var(--ink)}
.list{list-style:none;font-size:11.5px;line-height:18px;color:var(--ink)}
.list li{display:flex;align-items:center;gap:6px;white-space:nowrap}
.list li::before{content:"";width:7px;height:7px;border-radius:50%;background:currentColor;flex:none}
.list.on-dark{color:var(--white)}
.list.on-dark li::before{background:var(--yellow)}
.duration{display:flex;flex-direction:column;border:2px solid var(--orange);border-radius:14px;overflow:hidden;background:var(--white)}
.duration .len{flex:1;display:flex;flex-direction:column;align-items:center;justify-content:center;color:var(--ink);font-weight:700;line-height:.95}
.duration .num{font-size:40px}
.duration .unit{font-size:20px;font-weight:600}
.duration .start{height:46%;background:var(--purple);border-top:2px solid var(--orange);border-radius:12px;color:var(--white);font-size:24px;font-weight:500;display:flex;align-items:center;justify-content:center}
.accent{color:var(--yellow);font-weight:700;font-size:22px;line-height:1.1}
.white-h{color:var(--white);font-weight:700;font-size:19px;line-height:1.05}
.date-tag{border:2px solid var(--yellow);border-radius:12px;background:var(--purple);color:var(--white);font-size:24px;font-weight:500;display:flex;align-items:center;justify-content:center}
</style>
</head>
<body>
<main class="ad">
  <div class="band-top"></div>
  <div class="band-yellow"></div>
  <div class="band-lower"></div>

  <div class="abs photo" role="img" aria-label="Photo of a smiling young professional in glasses and a white collared shirt, arms crossed"></div>

  <div class="abs script">Skill up Salary up</div>
  <h1 class="abs headline upcoming">UPCOMING</h1>
  <div class="abs headline courses">SUMMIT COURSES</div>

  <div class="abs perk" style="left:58px"><svg width="15" height="15" viewBox="0 0 16 16"><circle cx="8" cy="8" r="8" fill="#fdc000"/><path d="M4.5 8.2l2.3 2.3 4.7-4.7" stroke="#4b0a6e" stroke-width="2" fill="none"/></svg><span>Men &amp;<br>Women</span></div>
  <div class="abs perk" style="left:198px"><svg width="15" height="15" viewBox="0 0 16 16"><circle cx="8" cy="8" r="8" fill="#fdc000"/><path d="M4.5 8.2l2.3 2.3 4.7-4.7" stroke="#4b0a6e" stroke-width="2" fill="none"/></svg><span>In-Person<br>&amp; Remote</span></div>
  <div class="abs perk" style="left:366px"><svg width="15" height="15" viewBox="0 0 16 16"><circle cx="8" cy="8" r="8" fill="#fdc000"/><path d="M4.5 8.2l2.3 2.3 4.7-4.7" stroke="#4b0a6e" stroke-width="2" fill="none"/></svg><span>Partial<br>Scholorships</span></div>

  <!-- Vocational Horizon Course -->
  <div class="abs pill dark" style="left:56px;top:347px;width:285px;height:42px">Vocational Horizon</div>
  <div class="abs subhead" style="left:58px;top:402px">Business Skills &amp;<br>Knowledge to:</div>
  <ul class="abs list" style="left:58px;top:446px">
    <li>Impress your interviewer</li><li>Maximize Income</li><li>Start / Run Your Business</li>
  </ul>
  <div class="abs duration" style="left:310px;top:397px;width:147px;height:103px">
    <div class="len"><span class="num" style="font-size:32px">4-5</span><span class="unit">MONTHS</span></div>
    <div class="start">NOV 2025</div>
  </div>
  <div class="abs subhead" style="left:56px;top:510px">Partial listing</div>
  <ul class="abs list" style="left:56px;top:536px"><li>Computers</li><li>Marketing</li><li>Sales</li><li>Finance</li></ul>
  <ul class="abs list" style="left:187px;top:536px"><li>Healthcare</li><li>Business Strategy</li><li>Communication</li><li>LedgerBooks</li></ul>
  <ul class="abs list" style="left:356px;top:536px"><li>Investments</li><li>Real Estate</li><li>Accounting</li></ul>

  <!-- IT support -->
  <div class="abs pill warm" style="left:58px;top:651px;width:426px;height:42px">IT Desktop &amp; Networking Support</div>
  <div class="abs accent" style="left:58px;top:703px">#2 Best Job</div>
  <div class="abs white-h" style="left:58px;top:732px">National Career<br>Review 2025</div>
  <div class="abs accent" style="left:58px;top:778px;font-size:19px">Masters IT</div>
  <ul class="abs list on-dark" style="left:58px;top:801px"><li>Desktop OS</li><li>Servers</li></ul>
  <ul class="abs list on-dark" style="left:123px;top:801px"><li>Networks</li><li>Cloud</li></ul>
  <div class="abs duration" style="left:284px;top:714px;width:150px;height:104px">
    <div class="len"><span class="num">7</span><span class="unit">MONTHS</span></div>
    <div class="start">DEC 2025</div>
  </div>

  <!-- Software -->
  <div class="abs pill warm" style="left:539px;top:651px;width:307px;height:42px">Software, Web &amp; Apps</div>
  <div class="abs accent" style="left:539px;top:703px">#2 Best Tech Job</div>
  <div class="abs white-h" style="left:539px;top:732px">National Career<br>Review 2025</div>
  <div class="abs date-tag" style="left:765px;top:704px;width:149px;height:44px">NOV 2025</div>
  <div class="abs accent" style="left:539px;top:778px;font-size:19px">Job Opportunities</div>
  <ul class="abs list on-dark" style="left:539px;top:801px"><li>Computer Programmer</li><li>Software Developer/Mobile</li></ul>
  <ul class="abs list on-dark" style="left:730px;top:801px;line-height:18px"><li>Engineer Developer (Apps)</li><li>Optional: Bachelors in Prog.</li></ul>
  <div class="abs" style="left:743px;top:834px;color:#fff;font-size:11.5px">&amp; Tech</div>

  <!-- Bookkeeping -->
  <div class="abs pill warm" style="left:58px;top:875px;width:341px;height:42px">Bookkeeping LedgerBooks</div>
  <div class="abs white-h" style="left:58px;top:930px">Train for a quality job<br>Manage your<br>own books</div>
  <ul class="abs list on-dark" style="left:58px;top:992px"><li>Finance Management</li><li>Customer &amp; Vendor Mgmt</li><li>Advanced Tools</li></ul>
  <div class="abs duration" style="left:309px;top:933px;width:149px;height:105px">
    <div class="len"><span class="num">5</span><span class="unit">weeks</span></div>
    <div class="start">NOV 2025</div>
  </div>

  <!-- Office -->
  <div class="abs pill warm" style="left:539px;top:875px;width:375px;height:42px">Office Suite- Computers</div>
  <div class="abs accent" style="left:539px;top:932px;font-size:18px;line-height:1">The New<br>Job Prerequisite</div>
  <ul class="abs list on-dark" style="left:539px;top:976px"><li>Sheets</li><li>Docs</li></ul>
  <ul class="abs list on-dark" style="left:611px;top:976px"><li>Email</li><li>Slides</li></ul>
  <div class="abs accent" style="left:539px;top:1020px;font-size:17px;line-height:1.05">Computer lab<br><span style="color:#fff">available to practice</span></div>
  <div class="abs duration" style="left:748px;top:931px;width:149px;height:105px">
    <div class="len"><span class="num">5</span><span class="unit">Weeks</span></div>
    <div class="start">DEC 2025</div>
  </div>
</main>
</body>
</html>
```